A simple Chatterbook Ad (not Chatterbook Page) for weight loss surgery

It’s a simple ad in terms of the text.

The text should say:
Curious about weight loss surgery?
This 30 second quiz will tell you which procedure will suit you best

I'm open to variations in the text if it is thought to enhance the ad.

Targeted towards obese individuals who have been unable to lose weight with diet and exercise. My industry is weight loss surgery – webpage www.marcusbellweather.com.au. Clicking the ad leads to a quiz on my webpage relating to weight loss surgery. Most frequent users of this service are females (75%) between ages of 35 and 55 years.

Successful weight loss surgery can enable individuals who have been unable to lose weight to lose a substantial amount of the excess weight they are carrying to be healthier and happier.

```html
<!DOCTYPE html>
<html lang="en">
<head>
<meta charset="UTF-8">
<title>Weight Loss Surgery Quiz Ad</title>
<link rel="stylesheet" href="https://fonts.googleapis.com/css2?family=Barlow+Condensed:wght@300;400;500;600;700&display=swap">
<style>
  :root {
    --stage: #272727;
    --teal: #1db6b0;
    --teal-deep: #17a8a5;
    --purple: #6b54b6;
    --violet: #5f63bd;
    --lavender: #9ca6e4;
    --white: #ffffff;
    --qmark-soft: rgba(220,228,245,0.9);
  }
  * { margin: 0; padding: 0; box-sizing: border-box; }
  html, body { width: 1200px; height: 1177px; overflow: hidden; background: var(--stage); }
  .ad {
    position: absolute; left: 178px; top: 150px; width: 862px; height: 862px; overflow: hidden;
    background: linear-gradient(180deg, var(--teal) 0%, #2aa9b7 30%, var(--violet) 62%, var(--purple) 100%);
    font-family: "Barlow Condensed", "Arial Narrow", sans-serif; color: var(--white);
  }
  .layer { position: absolute; left: 0; top: 0; width: 862px; height: 862px; }
  .eyebrow {
    position: absolute; left: 0; width: 500px; top: 51px;
    font-weight: 300; font-size: 64px; letter-spacing: 1.5px; line-height: 1;
    text-align: center; white-space: nowrap;
  }
  .dots {
    position: absolute; left: 68px; top: 122px; width: 357px; height: 0;
    border-top: 4px dotted rgba(255,255,255,0.9);
  }
  .headline {
    position: absolute; left: 0; width: 500px; font-weight: 600; line-height: 1;
    text-align: center; white-space: nowrap; transform-origin: 246px 50%;
  }
  .headline.line-one { top: 146px; font-size: 100px; transform: scaleX(0.78); }
  .headline.line-two { top: 231px; font-size: 136px; transform: scaleX(0.88); }
  .qmark { position: absolute; font-weight: 600; line-height: 1; text-align: center; }
  .qmark.main { left: 181px; width: 120px; top: 360px; font-size: 220px; color: var(--white); }
  .qmark.side { width: 100px; top: 395px; font-size: 130px; color: var(--qmark-soft); }
  .qmark.left { left: 101px; transform: rotate(-14deg); }
  .qmark.right { left: 272px; transform: rotate(14deg); }
  .quiz-button {
    position: absolute; left: 44px; top: 596px; width: 432px; height: 70px;
    border-radius: 35px; border: 4px solid rgba(255,255,255,0.9);
    background: linear-gradient(180deg, #3fcfc8 0%, var(--teal-deep) 100%);
    box-shadow: 0 4px 8px rgba(40,30,90,0.35);
    font-weight: 600; font-size: 48px; line-height: 62px; text-align: center; white-space: nowrap;
  }
  .subline {
    position: absolute; left: 0; width: 460px; top: 684px;
    font-weight: 400; font-size: 34px; line-height: 36px; text-align: center;
  }
  .brand { position: absolute; left: 540px; top: 790px; display: flex; align-items: center; gap: 12px; }
  .brand-mark { width: 34px; height: 34px; border-radius: 50%; background: var(--teal-deep); }
  .brand-name { font-weight: 500; font-size: 30px; letter-spacing: 1.5px; color: var(--teal-deep); line-height: 1; white-space: nowrap; }
  .brand-role { font-weight: 500; font-size: 14px; letter-spacing: 1px; color: var(--teal-deep); line-height: 1.2; white-space: nowrap; }
</style>
</head>
<body>
  <div class="ad">
    <svg class="layer" viewBox="0 0 862 862" role="img" aria-label="Photo of a slim woman in white underwear standing in profile, with a drawn outline of a larger body and arrows around her">
      <path d="M660 0 L862 0 L862 862 L600 862 C560 760 520 620 490 480 C450 330 520 120 660 0 Z" fill="var(--lavender)"/>
    </svg>
    <svg class="layer" viewBox="0 0 862 862" aria-hidden="true">
      <defs>
        <linearGradient id="edge" x1="0" y1="0" x2="0" y2="1">
          <stop offset="0" stop-color="#1db6b0"/>
          <stop offset="1" stop-color="#6b54b6"/>
        </linearGradient>
        <linearGradient id="base-edge" x1="0" y1="0" x2="1" y2="0">
          <stop offset="0" stop-color="#6b54b6"/>
          <stop offset="1" stop-color="#1db6b0"/>
        </linearGradient>
      </defs>
      <path d="M646 0 C506 120 436 330 476 480 C506 620 546 760 586 862" fill="none" stroke="url(#edge)" stroke-width="10"/>
      <path d="M660 0 C520 120 450 330 490 480 C520 620 560 760 600 862" fill="none" stroke="var(--white)" stroke-width="7"/>
      <path d="M346 862 C470 752 650 694 862 696" fill="none" stroke="url(#base-edge)" stroke-width="12"/>
      <path d="M362 862 C480 762 650 706 862 708 L862 862 Z" fill="var(--white)"/>
    </svg>

    <div class="eyebrow">CURIOUS ABOUT</div>
    <div class="dots"></div>
    <div class="headline line-one">WEIGHT LOSS</div>
    <div class="headline line-two">SURGERY</div>

    <div class="qmark side left">?</div>
    <div class="qmark main">?</div>
    <div class="qmark side right">?</div>

    <div class="quiz-button">THIS 30 SECOND QUIZ</div>
    <div class="subline">will tell you<br>which procedure<br>will suit you best</div>

    <div class="brand">
      <div class="brand-mark"></div>
      <div>
        <div class="brand-name">MARCUS BELLWEATHER</div>
        <div class="brand-role">GENERAL, UPPER GI &amp; BARIATRIC SURGEON</div>
      </div>
    </div>
  </div>
</body>
</html>
```